Healthcare Service Provider looking for PowerPoint Template

ROV Profile of the company & business activity
===================================
ROV is the leading after-sale healthcare services provider in Kuwait. The IT department in the company sells & executes Healthcare IT projects in hospitals that mainly cover:

1. IT Infrastructure covering data center, disaster recovery, servers, virtualization, backup, redundancy & high-availability, multi-site connectivity, wired & wireless networking, OS & network management, software subscriptions, …etc.

2. Healthcare IT systems covering the Hospital Management system, Electronic Medical Record, evidence-based clinical content, clinical decision support systems, Radiology information system, Lab information system, pharmacy management system, ICU system, dental system, dietary & nutrition system, integration with 3rd party systems in the hospital

3. Human resources covering the company specialized teams of clinical informatics specialists, pharmacists, nurses, project managers, user experience specialists, integration specialists, systems analysts, systems developers, DB administrators, Network administrators, system architects, systems engineers, …

The assortment of these professionals handle the services for implementing specialty Healthcare IT systems, training hospital staff & healthcare professionals, on-site support & maintenance of implemented healthcare systems at the hospital

Requested design job
================
We require a PowerPoint template to be used by the IT department in presenting sales & marketing pitches, commercial proposals, projects, and related to the business activities described in the profile.

The design of the PowerPoint template should:

. be personalized for the business activities of the IT department. promote the corporate brand identity of the company. provide clean, modern and fluent look & feel for presenting on screen, projector or printing. include font selection & design as part of the template design. light colored background

. multiple page layouts & slide types like a cover slide, title slide, different types of content slides, ….

. include design collaterals like icons and clip-arts

. have common design elements in PowerPoint Master slides

Included are the current corporate logos of the company.

In summary, simplicity, fluency and personality are key to the design we seek.

Requirements
Must have
• The design of the PowerPoint template should:
• . be personalized for the business activities of the IT department. promote the corporate brand identity of the company. provide clean, modern and fluent look & feel for presenting on screen, projector or printing. include font selection & design as part of the template design. light colored background
• . multiple page layouts & slide types like a cover slide, title slide, different types of content slides, ….
• . include design collaterals like icons and clip-arts
• . have common design elements in PowerPoint Master slides

```html
<!DOCTYPE html>
<html lang="en">
<head>
<meta charset="utf-8">
<title>ROV – Testing Team</title>
<link rel="stylesheet" href="https://fonts.googleapis.com/css2?family=Lato:wght@300;700;900&display=swap">
<style>
  :root {
    --tint-deep: #5f86cc;
    --tint-mid: #86a0d9;
    --tint-light: #9aaade;
    --tint-glow: #c3cff0;
    --text-white: #ffffff;
    --text-soft: #f2f5fc;
  }
  * { margin: 0; padding: 0; box-sizing: border-box; }
  html, body {
    width: 1200px;
    height: 684px;
    overflow: hidden;
    background: var(--tint-mid);
  }
  .slide {
    position: relative;
    width: 1200px;
    height: 684px;
    overflow: hidden;
    font-family: "Lato", Arial, sans-serif;
    color: var(--text-white);
    background: linear-gradient(100deg, var(--tint-mid) 0%, var(--tint-light) 100%);
  }
  .slide__photo {
    position: absolute;
    left: 0;
    top: 0;
    width: 900px;
    height: 684px;
    background:
      radial-gradient(ellipse 260px 300px at 210px 300px, rgba(220,230,250,0.55), transparent 70%),
      radial-gradient(ellipse 200px 160px at 320px 140px, rgba(60,95,170,0.55), transparent 75%),
      radial-gradient(ellipse 160px 260px at 780px 560px, rgba(200,215,245,0.45), transparent 75%),
      radial-gradient(ellipse 40px 120px at 860px 600px, rgba(40,80,190,0.55), transparent 80%),
      linear-gradient(90deg, var(--tint-deep) 0%, rgba(110,145,210,0.85) 45%, rgba(134,160,217,0) 100%);
  }
  .brand {
    position: absolute;
    top: 18px;
    right: 12px;
    width: 135px;
    text-align: center;
    font-weight: 900;
    font-size: 50px;
    letter-spacing: 4px;
    line-height: 1;
    color: var(--text-white);
  }
  .content {
    position: absolute;
    left: 530px;
    top: 266px;
    width: 572px;
  }
  .content__title {
    font-weight: 700;
    font-size: 60px;
    line-height: 1;
    letter-spacing: 0.3px;
    text-transform: uppercase;
  }
  .content__body {
    margin-top: 16px;
    margin-left: 6px;
    width: 566px;
    font-weight: 300;
    font-size: 22px;
    line-height: 37px;
    text-align: justify;
    color: var(--text-soft);
  }
  .page-number {
    position: absolute;
    right: 16px;
    bottom: 12px;
    font-weight: 700;
    font-size: 14px;
  }
</style>
</head>
<body>
  <div class="slide">
    <div class="slide__photo" role="img" aria-label="Blue-tinted photograph of a lab scientist in mask and safety goggles holding a blue test tube, overlaid with faint technology interface graphics"></div>

    <div class="brand">ROV</div>

    <section class="content">
      <h1 class="content__title">Testing Team</h1>
      <p class="content__body">Liquorice chupa chups applicake apple pie cupcake brownie bear claw cake gingerbread cotton candy. Bear claw croissant apple pie. Croissant cake sweet puff oreo. Liquorice chupa chups applicake apple pie cupcake brownie bear claw cake gingerbread cotton candy.</p>
    </section>

    <div class="page-number">02</div>
  </div>
</body>
</html>
```